Shine4all

Full service cleaning company. Specializing in commercial and apartment cleans.
Fully licensed and insured
Digital photos and invoices provided
for every job
For web designer...basic info as expected by a highend cleaning company that provides excellent service at reasonable pricing. We are going after large property management companies as well as not pricing ourselves out to help the local mom and pop companies as well.
Updates

Project Deadline Extended Reason: Everyone seems to be having trouble understanding that we are a dumpster company that is adding a cleaning side to the company. We want our clients to see Shine4All as a separate branch of our our already established waste management company.We are not a regular cleaning company. We specialize in going after large commercial cleans and apartment cleans. I have now included info regarding a proposal for work and our invoice/job completion to make it clearer what we do Added Monday, July 20, 2015

Target Market(s)

Property Management companies in Savannah, Richmond Hill, Rincon, Hinesville and Midway Georgia

Industry/Entity Type

Cleaning Service

Coding

Coded - Design and coding required

Number of Pages Required

3 page

Requirements
Must have
• Nice home page with lots of photos (stock are fine) to convey exactly what we do (getting logo bid on right now on this sight).
• Information page with employee photos (can leave blank) need room for 4 photos and bios.
• Page or link to a static page for the dumpster company BinTrek (logo for this is red and black file attached along with photo of dumpster. This page just needs to be one page with contact info and information about commercial dumpster.
• Basically this site is just a fluff page used for marketing purposes. Its content can be general and once created wont change much. Services and photos can be provided upon request but general layout and info is what we are looking for.

```html
<!DOCTYPE html>
<html lang="en">
<head>
<meta charset="utf-8">
<title>Shine4All</title>
<link href="https://fonts.googleapis.com/css2?family=Noto+Serif:wght@400;700&family=Open+Sans:wght@400;600;700&display=swap" rel="stylesheet">
<style>
:root{
  --red:#e0262a;
  --red-dark:#b81c20;
  --ink:#1d1d1d;
  --text:#6f6f6f;
  --muted:#9a9a9a;
  --band:#eeeeee;
  --line:#dcdcdc;
  --green:#8cb82a;
  --green-dark:#6f9618;
  --footer:#1f1f1f;
  --footer-deep:#111111;
  --white:#ffffff;
}
*{margin:0;padding:0;box-sizing:border-box}
html,body{width:681px;height:1200px;overflow:hidden;background:var(--white)}
body{font-family:"Open Sans",Arial,sans-serif;font-size:6.5px;color:var(--text);line-height:1.5}
h2,h3{font-family:"Noto Serif",Georgia,serif;color:var(--ink);font-weight:700}
.wrap{width:600px;margin:0 auto;position:relative}

/* header */
.site-header{height:80px;position:relative}
.brand{position:absolute;left:0;top:12px;display:flex;align-items:center;gap:6px}
.brand-mark{width:22px;height:22px;background:var(--red)}
.brand-name{font-family:"Open Sans",Arial,sans-serif;font-weight:700;font-size:19px;color:var(--ink)}
.contact-top{position:absolute;right:0;top:6px;display:flex;align-items:center;gap:10px;font-size:7px;color:var(--ink)}
.contact-top .mail{display:flex;align-items:center;gap:4px}
.phone-pill{background:var(--red);color:var(--white);font-weight:700;font-size:11px;padding:3px 12px;border-radius:12px;display:flex;align-items:center;gap:5px}
.main-nav{position:absolute;right:0;top:56px;display:flex;background:var(--red);height:22px}
.main-nav a{color:var(--white);text-decoration:none;font-size:7px;font-weight:600;padding:0 11px;line-height:22px}
.main-nav a.active{background:var(--ink)}

/* hero */
.hero{height:252px;position:relative;background:linear-gradient(100deg,#c4cad0 0%,#8a9690 30%,#4f6a4f 45%,#a9b3bd 60%,#7e8b99 80%,#d9dde2 100%)}
.hero-copy{position:absolute;left:380px;top:78px;color:var(--white);font-weight:700;font-size:11px;line-height:1.45}
.hero-copy span{display:inline-block;background:rgba(0,0,0,.55);padding:1px 6px;margin-bottom:2px}
.hero-dots{position:absolute;right:40px;bottom:10px;display:flex;gap:4px}
.hero-dots i{width:6px;height:6px;border-radius:50%;background:var(--red);opacity:.5}
.hero-dots i:first-child{opacity:1}

/* services band */
.services{background:var(--band);padding:22px 0 20px}
.services .wrap{display:flex;gap:20px}
.service-card{flex:1;background:var(--white);border-top:3px solid var(--red);padding:8px 8px 10px}
.service-card h3{font-size:12px;margin-bottom:6px}
.service-card .photo{height:66px;margin-bottom:7px}
.service-card p{font-size:6px}
.read-more{display:block;text-align:right;color:var(--red);font-weight:700;font-size:6px;margin-top:6px}

/* welcome + schedule */
.intro{padding:24px 0 20px;border-bottom:1px solid var(--line)}
.intro .wrap{display:flex;gap:24px}
.welcome{flex:1.9}
.welcome h2,.schedule h2{font-size:13px;margin-bottom:9px}
.welcome p{margin-bottom:8px;font-size:6.2px}
.schedule{flex:1}
.schedule form{display:flex;flex-direction:column;gap:5px}
.field{height:14px;border:1px solid var(--line);background:#f7f7f7;font-size:5.5px;color:var(--muted);padding:2px 5px}
.field-row{display:flex;gap:5px}.field-row .field{flex:1}
.field.area{height:32px}
.send{align-self:flex-end;background:var(--red);color:var(--white);font-size:6px;font-weight:700;padding:3px 10px;border:0}

/* features */
.features{padding:22px 0 18px}
.features .wrap{display:flex;gap:20px}
.feature{flex:1}
.feature h3{font-size:11px;margin-bottom:8px}
.feature .photo{height:70px;margin-bottom:7px}
.checks{list-style:none}
.checks li{display:flex;align-items:center;gap:5px;font-size:6px;padding:3px 0;border-bottom:1px dotted var(--line)}

/* cta */
.cta{background:var(--green);height:52px;display:flex;align-items:center;justify-content:center;gap:14px;border-top:3px solid var(--green-dark)}
.cta p{color:var(--white);font-family:"Noto Serif",Georgia,serif;font-weight:700;font-size:11px}
.cta .btn{background:var(--footer-deep);color:var(--white);font-size:6px;font-weight:700;padding:5px 10px}

/* footer */
.site-footer{background:var(--footer);margin-top:14px;height:102px;padding-top:12px;color:#b5b5b5}
.site-footer .wrap{display:flex;gap:22px}
.foot-col h4{color:var(--white);font-size:8px;font-weight:600;margin-bottom:6px}
.foot-col ul{list-style:none}
.foot-col li{font-size:5.5px;line-height:1.65}
.quick{width:120px}.info{width:140px}.faq{width:160px}
.info li{display:flex;gap:4px;align-items:flex-start}
.foot-brand{margin-left:auto;display:flex;align-items:center;gap:5px;margin-top:20px}
.foot-brand .brand-mark{width:16px;height:16px;background:#555}
.foot-brand span{font-weight:700;font-size:15px;color:#6c6c6c}
.bottom-bar{background:var(--footer-deep);height:16px}
.bottom-bar .wrap{display:flex;justify-content:space-between;align-items:center;height:16px;font-size:5px;color:#8a8a8a}
.social{display:flex;gap:3px}
.social i{width:8px;height:8px;background:var(--red)}
</style>
</head>
<body>

<header class="site-header wrap">
  <div class="brand"><span class="brand-mark"></span><span class="brand-name">Shine4All</span></div>
  <div class="contact-top">
    <span class="mail">
      <svg width="8" height="6" viewBox="0 0 8 6"><rect x=".5" y=".5" width="7" height="5" fill="none" stroke="#e0262a"/><path d="M.5 .5 4 3.5 7.5 .5" fill="none" stroke="#e0262a"/></svg>
      info@shine4all.com
    </span>
    <span class="phone-pill">
      <svg width="8" height="8" viewBox="0 0 10 10"><path d="M2 1 4 1 5 3.5 3.8 4.5C4.4 5.8 5.2 6.6 6.5 7.2L7.5 6 9 7V9C5 9 1 5 1 1Z" fill="#fff"/></svg>
      123-456-7890
    </span>
  </div>
  <nav class="main-nav">
    <a class="active">Home</a><a>About Us</a><a>Services</a><a>Think Green</a><a>Customer Reviews</a><a>Contact Us</a>
  </nav>
</header>

<section class="hero" role="img" aria-label="Photo of a green roll-off waste truck beside tall apartment buildings">
  <div class="hero-copy">
    <span>We Are A Full Service Cleaning Company</span><br>
    <span>Specializing in commercial and</span><br>
    <span>apartment cleans</span>
  </div>
  <div class="hero-dots"><i></i><i></i><i></i></div>
</section>

<section class="services">
  <div class="wrap">
    <article class="service-card">
      <h3>Home Owner</h3>
      <div class="photo" role="img" aria-label="Photo of a loaded dumpster at a home" style="background:linear-gradient(135deg,#7a6a55,#a88c64 50%,#5d5145)"></div>
      <p>Lorem ipsum dolor sit amet, consectetur adipiscing elit. Phasellus volutpat ultricies euismod. Mauris consectetur tellus quis nisl dictum pharetra.</p>
      <span class="read-more">READ MORE &gt;</span>
    </article>
    <article class="service-card">
      <h3>Business Owner</h3>
      <div class="photo" role="img" aria-label="Photo of an orange commercial dumpster" style="background:linear-gradient(135deg,#3c5a78,#c2622b 45%,#d5874a 70%,#6b7c8c)"></div>
      <p>Lorem ipsum dolor sit amet, consectetur adipiscing elit. Phasellus volutpat ultricies euismod. Mauris consectetur tellus quis nisl dictum pharetra.</p>
      <span class="read-more">READ MORE &gt;</span>
    </article>
    <article class="service-card">
      <h3>Rent-a-Dumpster</h3>
      <div class="photo" role="img" aria-label="Photo of a roll-off dumpster container" style="background:linear-gradient(135deg,#e6eaf0,#4f78a8 50%,#d9dde2)"></div>
      <p>Lorem ipsum dolor sit amet, consectetur adipiscing elit. Phasellus volutpat ultricies euismod. Mauris consectetur tellus quis nisl dictum pharetra.</p>
      <span class="read-more">READ MORE &gt;</span>
    </article>
  </div>
</section>

<section class="intro">
  <div class="wrap">
    <div class="welcome">
      <h2>Welcome To Shine4All</h2>
      <p>Lorem ipsum dolor sit amet, consectetuer adipiscing elit, sed diam nonummy nibh euismod tincidunt ut laoreet dolore magna aliquam erat volutpat. Ut wisi enim ad minim veniam, quis nostrud exerci tation ullamcorper suscipit lobortis nisl ut aliquip ex ea commodo consequat.</p>
      <p>Lorem ipsum dolor sit amet, consectetuer adipiscing elit, sed diam nonummy nibh euismod tincidunt ut laoreet dolore magna aliquam erat volutpat. Ut wisi enim ad minim veniam, quis nostrud exerci tation ullamcorper suscipit lobortis nisl ut aliquip ex ea commodo consequat.</p>
      <span class="read-more">READ MORE &gt;</span>
    </div>
    <div class="schedule">
      <h2>Schedule A Service</h2>
      <form>
        <div class="field">Name</div>
        <div class="field">Phone</div>
        <div class="field-row"><div class="field">Pick up Date</div><div class="field">Time</div></div>
        <div class="field">Email</div>
        <div class="field area">Message</div>
        <button class="send" type="button">SEND</button>
      </form>
    </div>
  </div>
</section>

<section class="features">
  <div class="wrap">
    <div class="feature">
      <h3>24/7 Access</h3>
      <div class="photo" role="img" aria-label="Photo of a 24 hour service sign" style="background:linear-gradient(135deg,#2d3440,#9aa4b0 50%,#3a4250)"></div>
      <p>Lorem ipsum dolor sit amet consectetur adipiscing elit sed do eiusmod tincidunt laoreet dolore magna aliquam.</p>
    </div>
    <div class="feature">
      <h3>Reliable. Clean. Safe.</h3>
      <div class="photo" role="img" aria-label="Photo of a row of green dumpsters" style="background:linear-gradient(135deg,#9fc6e0,#3f9a4a 45%,#2f7d3a 75%,#a9c99a)"></div>
      <p>Lorem ipsum dolor sit amet consectetur adipiscing elit sed do eiusmod tincidunt laoreet dolore magna aliquam.</p>
    </div>
    <div class="feature">
      <h3>Why Choose Us</h3>
      <ul class="checks">
        <li><svg width="6" height="6" viewBox="0 0 6 6"><path d="M.5 3 2.3 5 5.5 .8" fill="none" stroke="#e0262a" stroke-width="1.2"/></svg>Wide selection of dumpster sizes available</li>
        <li><svg width="6" height="6" viewBox="0 0 6 6"><path d="M.5 3 2.3 5 5.5 .8" fill="none" stroke="#e0262a" stroke-width="1.2"/></svg>Flexible, timely pickup and delivery</li>
        <li><svg width="6" height="6" viewBox="0 0 6 6"><path d="M.5 3 2.3 5 5.5 .8" fill="none" stroke="#e0262a" stroke-width="1.2"/></svg>Fast service anywhere</li>
        <li><svg width="6" height="6" viewBox="0 0 6 6"><path d="M.5 3 2.3 5 5.5 .8" fill="none" stroke="#e0262a" stroke-width="1.2"/></svg>Easy online ordering and scheduling</li>
        <li><svg width="6" height="6" viewBox="0 0 6 6"><path d="M.5 3 2.3 5 5.5 .8" fill="none" stroke="#e0262a" stroke-width="1.2"/></svg>Online account management</li>
        <li><svg width="6" height="6" viewBox="0 0 6 6"><path d="M.5 3 2.3 5 5.5 .8" fill="none" stroke="#e0262a" stroke-width="1.2"/></svg>Instant online pricing</li>
      </ul>
    </div>
  </div>
</section>

<section class="cta">
  <p>Ready to get started? See what dumpsters are available in your area.</p>
  <span class="btn">SHOW PRODUCTS</span>
</section>

<footer>
  <div class="site-footer">
    <div class="wrap">
      <div class="foot-col quick">
        <h4>Quick Links</h4>
        <ul><li>Home</li><li>About Us</li><li>Services</li><li>Think Green</li><li>Customer Reviews</li><li>Contact Us</li></ul>
      </div>
      <div class="foot-col info">
        <h4>Contact Information</h4>
        <ul>
          <li><svg width="5" height="7" viewBox="0 0 5 7"><path d="M2.5 7C1 5 0 3.8 0 2.5a2.5 2.5 0 0 1 5 0C5 3.8 4 5 2.5 7Z" fill="#e0262a"/></svg>Lorem ipsum dolor sit consectetur adipiscing elit, 100 Sample St, City, ST 00000</li>
          <li><svg width="6" height="6" viewBox="0 0 10 10"><path d="M2 1 4 1 5 3.5 3.8 4.5C4.4 5.8 5.2 6.6 6.5 7.2L7.5 6 9 7V9C5 9 1 5 1 1Z" fill="#e0262a"/></svg>123-456-7890</li>
          <li><svg width="7" height="5" viewBox="0 0 8 6"><rect x=".5" y=".5" width="7" height="5" fill="none" stroke="#e0262a"/></svg>info@shine4all.com</li>
        </ul>
      </div>
      <div class="foot-col faq">
        <h4>FAQ's</h4>
        <ul>
          <li>What sizes of dumpster do we offer?</li>
          <li>How much does a dumpster cost?</li>
          <li>How much does a cleaning cost?</li>
          <li>How long can we keep the dumpster?</li>
          <li style="color:var(--white)">More FAQS</li>
        </ul>
      </div>
      <div class="foot-brand"><span class="brand-mark"></span><span>Shine4All</span></div>
    </div>
  </div>
  <div class="bottom-bar">
    <div class="wrap">
      <span>&copy; 2015 Shine4All | All rights reserved</span>
      <span class="social"><i></i><i></i><i></i><i></i><i></i></span>
    </div>
  </div>
</footer>

</body>
</html>
```